Website for SaaS CRM software

We require a cool website for a new SaaS CRM software. The design needs to be slick and modern. I quite like the look of sites like PostOtter.

The character 'Marla' in the video is the main character which we would like to incorporate on each page if possible. Like the chimp on Postotter website.

'Sign Up Free' button or form to feature throughout the site so we have a strong call to action.

Here is a short video which will give you an idea of the software:
https://clipvault.example/83920417
Password: trelbq

You can login to the user software (backend) for screen grabs and to see what the software is all about:
www.taskloomhq.example
Username: tenant7
Password: tenant7

Please note: The website is for the front end which is where we sell the software and NOT once the user has logged in.

Target Market(s)

Small businesses, freelancers, designers, 1-man businesses

Industry/Entity Type

Software

Requirements
Must have
• 1. Opt-in box for getting started for free:

'Sign up for your Free account'

2. Logos for social media : Fb/Twitter/YouTube/LinkedIn / G+
3. Facebook 'LIKE' button
4.The Navigation Bar should always be on display at the top when scrolling
5. Login button near the Navigation Bar
6. Login page or pop-up should also have 'Forgot Password' link which prompts them to enter their email so a password can be emailed to them.

5 pages & a blog in total. The pages we require are:

HOME
- Heading 'Easy to use small business software'
- Should have a video placeholder and some bullet points or tick marks for key features. The video (from YouTube) should open up on a bigger lightbox and the background greyed out.
- Sign up box to have the fields for First Name, Company Name, Email & Password with a check box for 'I agree with Terms & Conditions'

TOUR
Sub-Navigation bar at the top or side bar with the headings for each module i.e CONTACTS, QUOTES, JOBS, DIARY, SALES, PURCHASES, PRODUCTS, REPORTS
Each module with need to have a placeholder for an image or video and 1 paragraph of text explaining key features. Please see http://postotter.example/features/

See how the Navigation buttons stay visible at all times and changes to the next button when scrolling: http://postotter.example/features/

No side bar on this page.

PRICING
Pricing table of 3 to 4 columns with a button at the bottom. This software is a monthly subscription, so we need to show the $/month for each Plan at the top with the name of the Plan
The plans are:
Bronze: Free
Silver: $20/month
Gold: $40 / month
Platinum: $75 / month

No side bar on this page.

Heading at the bottom: 'No minimum contract. Cancel anytime.'

SUPPORT PAGE
This to a contact form to submit a ticket for tech support. We also need a 2-column list for videos which we will put up. The video open up on a lightbox in bigger size.

No side bar on this page.

CONTACT
Contact details i.e name, address, telephone, email & a contact form
No side bar on this page.

BLOG
Pagecraft blog. I love the way the headings, paragraph, font, line spacing, colours are on the PostOtter blog.

Need a side bar.

```html
<!DOCTYPE html>
<html lang="en">
<head>
<meta charset="utf-8">
<title>Taskloom – Easy to use small Business Software</title>
<link rel="stylesheet" href="https://fonts.googleapis.com/css2?family=Open+Sans:wght@400;600;700&family=PT+Sans+Narrow:wght@700&family=Lato:ital,wght@0,400;0,700;1,400&display=swap">
<style>
:root{
  --blue:#2f9be6;
  --blue-light:#5cb8f2;
  --blue-deep:#1f86d6;
  --link:#1f8ad8;
  --ink:#222;
  --text:#555;
  --muted:#777;
  --rule:#e2e2e2;
  --dark:#333335;
  --footer:#2e2e30;
  --white:#fff;
}
*{box-sizing:border-box;margin:0;padding:0}
html,body{width:839px;height:1200px;overflow:hidden;background:var(--white)}
body{position:relative;font-family:"Lato",sans-serif;color:var(--text)}
.abs{position:absolute}

/* header */
.site-header{position:absolute;left:0;top:0;width:839px;height:88px;background:var(--white)}
.brand{position:absolute;left:34px;top:26px;font-family:"Open Sans",sans-serif;font-weight:700;font-size:34px;letter-spacing:-1px;color:#111;display:flex;align-items:center;gap:8px}
.brand-mark{width:14px;height:14px;border-radius:50%;background:var(--blue)}
.main-nav{position:absolute;left:378px;top:33px;height:40px;display:flex;border:1px solid #d8d8d8;border-radius:2px;background:linear-gradient(#fdfdfd,#ececec)}
.main-nav a{display:flex;align-items:center;justify-content:center;height:38px;font-family:"Open Sans",sans-serif;font-size:12px;color:#555;text-decoration:none;border-left:1px solid #dcdcdc}
.main-nav a:first-child{border-left:none}
.main-nav a.active{background:linear-gradient(var(--blue-light),var(--blue));color:var(--white)}

/* hero */
.hero{position:absolute;left:0;top:88px;width:839px;height:330px;background:radial-gradient(circle at 75% 30%,#7fcaf6 0,#45abec 45%,#2f9ae4 100%);border-bottom:3px solid var(--blue-deep);overflow:hidden}
.hero-ring{position:absolute;border:14px solid rgba(255,255,255,.08);border-radius:50%}
.hero-title{position:absolute;left:51px;top:56px;font-family:"Open Sans",sans-serif;color:var(--white);line-height:1.12}
.hero-title .l1{display:block;font-size:29px}
.hero-title .l2{display:block;font-size:33px}
.hero-sub{position:absolute;left:53px;top:135px;font-family:"PT Sans Narrow",sans-serif;font-weight:700;font-size:16px;color:var(--white)}
.hero-copy{position:absolute;left:51px;top:164px;width:310px;font-size:9.5px;line-height:16px;color:var(--white)}
.btn-video{position:absolute;left:50px;top:224px;width:113px;height:28px;background:#2b2b2b;border-radius:3px;color:var(--white);font-family:"PT Sans Narrow",sans-serif;font-weight:700;font-size:13px;display:flex;align-items:center;justify-content:center}
.hero-visual{position:absolute;left:368px;top:27px;width:422px;height:257px;border-radius:8px;background:linear-gradient(#4a4340,#2a2522 82%,#8a8582 84%,#5a5452)}
.hero-pager{position:absolute;left:378px;top:306px;width:80px;height:24px;background:var(--blue-light);clip-path:polygon(8px 0,72px 0,80px 100%,0 100%);display:flex;align-items:center;justify-content:center;gap:4px}
.hero-pager i{width:7px;height:7px;border-radius:50%;background:#d7efff}

/* content */
.section-title{font-family:"Open Sans",sans-serif;font-size:16.5px;color:var(--ink);font-weight:400}
.body-copy{font-size:9.3px;line-height:17px;color:var(--text)}
.lead{font-weight:700;color:#444}
.more{font-family:"Open Sans",sans-serif;font-size:9px;font-weight:600;color:#555;text-transform:uppercase;text-decoration:none}
.more.blue{color:var(--link)}

.welcome-photo{left:27px;top:476px;width:125px;height:94px;background:linear-gradient(135deg,#e9eef2,#b9c3cb 60%,#7d7068)}

.blog-title{font-family:"Open Sans",sans-serif;font-size:16.5px;color:var(--link)}
.post h3{font-family:"Open Sans",sans-serif;font-size:10px;font-weight:600;color:#222;margin-bottom:5px}
.post p{font-size:9.1px;line-height:14px;color:#555;margin-bottom:6px}

.divider{left:24px;top:725px;width:788px;height:1px;background:var(--rule)}

.video-frame{left:22px;top:775px;width:274px;height:192px;background:#3b3b3d;border:1px solid #2a2a2a}
.video-screen{position:absolute;left:6px;top:6px;width:261px;height:157px;background:linear-gradient(120deg,#dfe4e8,#c6ced5 45%,#8f9aa3 75%,#3a3e45)}
.video-bar{position:absolute;left:6px;top:168px;width:261px;height:18px;display:flex;align-items:center;gap:8px;padding:0 4px}
.play{width:17px;height:17px;border:1.5px solid #ddd;border-radius:50%;position:relative}
.play:after{content:"";position:absolute;left:6px;top:4px;border-left:6px solid #ddd;border-top:4px solid transparent;border-bottom:4px solid transparent}
.track{width:188px;height:3px;background:#eee}

.feature-lead{font-size:9.3px;line-height:17px;color:#555}
.checklist{list-style:none}
.checklist li{height:24.6px;border-bottom:1px solid #eee;display:flex;align-items:center;gap:8px;font-style:italic;font-size:9.1px;color:#555}
.checklist svg{flex:none}

/* signup */
.signup{left:563px;top:747px;width:243px;height:330px;background:linear-gradient(#fff,#f5f5f5);box-shadow:0 0 4px rgba(0,0,0,.12)}
.signup-head{height:40px;background:var(--dark);color:var(--white);font-family:"Open Sans",sans-serif;font-size:14px;padding:10px 21px}
.signup form{padding:14px 19px 0 18px}
.signup label{display:block;font-size:9.5px;color:#333;margin-bottom:5px}
.signup .field{width:203px;height:22px;border:1px solid #d6d6d6;border-radius:2px;background:var(--white);margin-bottom:15px}
.agree{display:flex;align-items:center;gap:6px;font-size:8.5px;color:#555;margin-top:-2px}
.agree span{width:13px;height:13px;border:1px solid #ccc;background:var(--white)}
.btn-signup{position:absolute;right:17px;top:280px;width:91px;height:26px;background:linear-gradient(var(--blue-light),var(--blue));color:var(--white);font-family:"PT Sans Narrow",sans-serif;font-weight:700;font-size:11.5px;display:flex;align-items:center;justify-content:center;border-radius:2px}

/* footer */
.site-footer{position:absolute;left:0;top:1119px;width:839px;height:81px;background:var(--footer)}
.footer-nav{position:absolute;left:32px;top:19px;font-size:9.5px;color:#e0e0e0;display:flex;gap:8px}
.footer-nav .sep{color:#999}
.copyright{position:absolute;left:33px;top:43px;font-size:8.3px;color:#bbb}
.stay{position:absolute;left:628px;top:21px;font-size:9.5px;color:#e6e6e6}
.social{position:absolute;left:714px;top:15px;display:flex;gap:6px}
.social i{width:17px;height:17px;border-radius:2px}
</style>
</head>
<body>

<header class="site-header">
  <div class="brand">taskloom<span class="brand-mark"></span></div>
  <nav class="main-nav">
    <a class="active" href="#" style="width:76px">Home</a>
    <a href="#" style="width:60px">Tour</a>
    <a href="#" style="width:71px">Pricing</a>
    <a href="#" style="width:81px">Support</a>
    <a href="#" style="width:75px">Contact</a>
    <a href="#" style="width:70px">Blog</a>
  </nav>
</header>

<section class="hero">
  <span class="hero-ring" style="left:-60px;top:-150px;width:360px;height:360px"></span>
  <span class="hero-ring" style="left:300px;top:-40px;width:160px;height:160px"></span>
  <span class="hero-ring" style="left:660px;top:-60px;width:240px;height:240px"></span>
  <h1 class="hero-title"><span class="l1">Easy to use small</span><span class="l2">Business Software</span></h1>
  <p class="hero-sub">Suspendisse quam leo, molestie sed luctus quis.</p>
  <p class="hero-copy">feugiat in, pede. Fusce tellus. Sed metus augue, convallis et, vehicula ut Pulvinar eu, ante. Integer orci tellus, tristique vitae, consequat nec, porta vel, lectus.</p>
  <a class="btn-video">Watch Our Video</a>
  <div class="hero-visual" role="img" aria-label="Laptop showing the software with contact, email and connection icons"></div>
  <div class="hero-pager"><i></i><i></i><i></i><i></i></div>
</section>

<h2 class="section-title abs" style="left:27px;top:443px">Welcome to Taskloom Website Mainpage..</h2>
<div class="welcome-photo abs" role="img" aria-label="Photo of a business team in a meeting"></div>
<p class="body-copy lead abs" style="left:161px;top:475px;width:355px">Pellentesque habitant morbi tristique senectus et netus et malesuada fames ac turpis egestas. In posuere felis nec tortor. Pellentesque faucibus.</p>
<p class="body-copy abs" style="left:161px;top:516px;width:355px">Ut accumsan ultricies elit. Maecenas at justo id velit placerat molestie. Donec dictum lectus non odio. Cras a ante vitae enim iaculis aliquam. Mauris nunc quam, venenatis nec, euismod sit amet, egestas placerat, est.</p>
<p class="body-copy abs" style="left:29px;top:577px;width:487px">Mauris vel lacus vitae felis vestibulum volutpat. Etiam est nunc, venenatis in, tristique eu, imperdiet ac, nisl. Cum sociis natoque penatibus et magnis dis parturient montes, nascetur ridiculus mus. In iaculis facilisis massa. Etiam eu urna. Sed porta. Suspendisse quam leo, molestie sed, luctus quis, feugiat in, pede.</p>
<p class="body-copy abs" style="left:29px;top:636px;width:487px">Fusce tellus. Sed metus augue, convallis et, vehicula ut, pulvinar eu, ante. Integer orci tellus, tristique vitae, consequat nec, porta vel, lectus. Nulla sit amet diam. Duis non nunc.v</p>
<a class="more abs" style="left:30px;top:682px">Learn More</a>

<h2 class="blog-title abs" style="left:556px;top:442px">Recent Blog Post</h2>
<article class="post abs" style="left:557px;top:474px;width:250px">
  <h3>Pellentesque nibh libero</h3>
  <p>Ultricies eu, sagittis non, mollis sed, justo. Praesent metus ipsum, pulvinar pulvinar, porta id, fringilla at, est.</p>
  <a class="more blue">Learn More</a>
</article>
<article class="post abs" style="left:558px;top:553px;width:250px">
  <h3>Quisque dignissim congue leo.</h3>
  <p>Ultricies eu, sagittis non, mollis sed, justo. Praesent metus ipsum, pulvinar pulvinar, porta id, fringilla at, est.</p>
  <a class="more blue">Learn More</a>
</article>
<article class="post abs" style="left:557px;top:637px;width:250px">
  <h3>Quisque dignissim congue leo.</h3>
  <p>Ultricies eu, sagittis non, mollis sed, justo. Praesent metus ipsum, pulvinar pulvinar, porta id, fringilla at, est.</p>
  <a class="more blue">Learn More</a>
</article>

<div class="divider abs"></div>

<h2 class="section-title abs" style="left:25px;top:741px">Check Out Our Features</h2>
<div class="video-frame abs">
  <div class="video-screen" role="img" aria-label="Video still of a businessman drawing a rising chart line"></div>
  <div class="video-bar">
    <span class="play"></span><span class="track"></span>
    <svg width="18" height="14" viewBox="0 0 18 14"><path d="M1 5h4l5-4v12l-5-4H1z" fill="none" stroke="#ddd" stroke-width="1.2"/><path d="M12 4q2 3 0 6M14 2q4 5 0 10" fill="none" stroke="#ddd" stroke-width="1.2"/></svg>
  </div>
</div>
<p class="feature-lead abs" style="left:314px;top:772px;width:215px"><b style="color:#444">Fusce tellus. Sed metus augue, convallis</b> et,vehicula ut, pulvinar eu, ante. Integer orci tellus, tristique vitae, consequat nec.</p>
<ul class="checklist abs" style="left:316px;top:831px;width:186px">
  <li><svg width="12" height="9" viewBox="0 0 12 9"><path d="M1 5l3 3 7-7" fill="none" stroke="#555" stroke-width="2.2"/></svg>Aliquam vehicula mi at mauris.</li>
  <li><svg width="12" height="9" viewBox="0 0 12 9"><path d="M1 5l3 3 7-7" fill="none" stroke="#555" stroke-width="2.2"/></svg>Maecenas placerat nisl at consequat</li>
  <li><svg width="12" height="9" viewBox="0 0 12 9"><path d="M1 5l3 3 7-7" fill="none" stroke="#555" stroke-width="2.2"/></svg>Rhoncus sem nunc gravida justo</li>
  <li><svg width="12" height="9" viewBox="0 0 12 9"><path d="M1 5l3 3 7-7" fill="none" stroke="#555" stroke-width="2.2"/></svg>Quis eleifend arcu velit quis lacus</li>
  <li style="border-bottom:none"><svg width="12" height="9" viewBox="0 0 12 9"><path d="M1 5l3 3 7-7" fill="none" stroke="#555" stroke-width="2.2"/></svg>Morbi magna magna</li>
</ul>
<p class="body-copy abs" style="left:25px;top:981px;width:490px;line-height:15.5px">Mauris vel lacus vitae felis vestibulum volutpat. Etiam est nunc, venenatis in, tristique eu, imperdiet ac, nisl. Cum sociis natoque penatibus et magnis dis parturient montes, nascetur ridiculus mus. In iaculis facilisis massa. Etiam eu urna. Sed porta. Suspendisse quam leo, molestie sed, luctus quis, feugiat in, pede.</p>
<p class="body-copy abs" style="left:25px;top:1034px;width:490px;line-height:15.5px">Fusce tellus. Sed metus augue, convallis et, vehicula ut, pulvinar eu, ante. Integer orci tellus, tristique vitae, consequat nec, porta vel, lectus. Nulla sit amet diam. Duis non nunc.v</p>

<aside class="signup abs">
  <div class="signup-head">Member Sign Up</div>
  <form>
    <label>First Name</label><div class="field"></div>
    <label>Company Name</label><div class="field"></div>
    <label>Email address</label><div class="field"></div>
    <label>Password</label><div class="field"></div>
    <div class="agree"><span></span>I agree with terms &amp; conditions</div>
  </form>
  <a class="btn-signup">SIGN UP NOW</a>
</aside>

<footer class="site-footer">
  <nav class="footer-nav"><span>Home</span><span class="sep">|</span><span>About Us</span><span class="sep">|</span><span>Press</span><span class="sep">|</span><span>Technology</span><span class="sep">|</span><span>Contact Us</span></nav>
  <p class="copyright">Copyright 2012 Quillfield Studio.&nbsp; All Rights Reserved</p>
  <span class="stay">Stay Connected</span>
  <div class="social"><i style="background:#3b5b98"></i><i style="background:#1a83c0"></i><i style="background:#e8741f"></i><i style="background:#d9d9d9"></i></div>
</footer>

</body>
</html>
```